Thornbury Lettings Managment Ltd website

Need a website To inform people/clients of the services we provide. 5 pages total with a local feel. Bristol, UK. I have logo artwork already is like the look based on
incorporate the artwork attached for theme, feel and colours fonts info etc

To best describe the business have a brief look at www.fernwickhomes.example.co.uk which is a local firm offering the same services. This is for your ref only and not to be copied.

Target Market(s)

Property Investors/Landlords

Coding

Coded - Design and coding required

Number of Pages Required

5+ page

Colors
0392cd
f68d4d

Requirements
Must have
• local feel. Possibly using some local architecture or historic landmarks etc. This is fexible.
• most also be mobile device compatible
Nice to have
• the membership logos - files attached: KTB, DWF, GMV and safehold-example.co.uk

```html
<!DOCTYPE html>
<html lang="en">
<head>
<meta charset="utf-8">
<title>Thornbury Lettings Managment Ltd</title>
<link href="https://fonts.googleapis.com/css2?family=Asap:wght@400;500;700&display=swap" rel="stylesheet">
<style>
:root{
  --blue:#0392cd;
  --blue-deep:#0a6fd6;
  --blue-bright:#1d8cf0;
  --orange:#f68d4d;
  --orange-soft:#f2a275;
  --charcoal:#2c2c2c;
  --topbar:#4a4a48;
  --footer:#1f1f1f;
  --footer-card:#3b3b3b;
  --brown:#6b3a1f;
  --white:#ffffff;
  --ink:#333333;
  --muted:#8a8a8a;
  --pale:#d7eef3;
}
*{box-sizing:border-box;margin:0;padding:0}
html,body{width:1200px;height:2609px;overflow:hidden}
body{font-family:"Asap",Arial,sans-serif;color:var(--ink);background:var(--white);position:relative}
.abs{position:absolute}
.section{position:absolute;left:0;width:1200px;overflow:hidden}

/* top bar */
.topbar{top:0;height:64px;background:linear-gradient(#55554f,#3f3f3c)}
.social{position:absolute;display:flex;gap:6px}
.social span{width:22px;height:22px;background:#8b8b86;display:block;border-radius:2px}
.topbar .social{left:307px;top:21px}
.top-links{position:absolute;right:301px;top:22px;color:#f0f0f0;font-size:13px;display:flex;gap:22px}
.top-links svg{vertical-align:-2px;margin-right:4px}

/* nav */
.navbar{top:64px;height:61px;background:var(--white);border-bottom:1px solid #e5e5e5}
.brand{position:absolute;left:301px;top:13px;display:flex;align-items:center;gap:10px}
.brand-mark{width:34px;height:34px;background:var(--blue)}
.brand-name{font-size:15px;font-weight:700;color:var(--charcoal);line-height:17px;width:150px}
.main-nav{position:absolute;left:557px;top:27px;display:flex;gap:15px;font-size:12px;font-weight:500;color:var(--charcoal)}
.main-nav .active{color:var(--orange);position:relative}
.main-nav .active::before{content:"";position:absolute;left:50%;top:-9px;width:4px;height:4px;margin-left:-2px;border-radius:50%;background:var(--orange)}

/* hero */
.hero{top:125px;height:480px;background:linear-gradient(180deg,#6d5a50 0%,#8a6d60 35%,#5f4e47 70%,#3c3431 100%)}
.hero-title{position:absolute;left:0;width:1200px;top:106px;text-align:center;color:var(--white);font-size:25px;font-weight:700}
.search-panel{position:absolute;left:299px;top:153px;width:600px;height:152px;background:var(--white)}
.search-panel .corner{position:absolute;bottom:0;width:0;height:0}
.corner.left{left:0;border-bottom:32px solid var(--blue);border-right:32px solid transparent}
.corner.right{right:0;border-bottom:32px solid var(--blue);border-left:32px solid transparent}
.field{position:absolute}
.field label{display:block;font-size:10px;color:var(--charcoal);margin-bottom:3px}
.field .select{height:15px;border:1px solid #c9c9c9;font-size:8px;color:#999;padding:1px 5px;position:relative}
.field .select::after{content:"";position:absolute;right:5px;top:5px;border-left:3px solid transparent;border-right:3px solid transparent;border-top:4px solid #777}
.search-btn{position:absolute;left:200px;top:115px;width:202px;height:37px;background:var(--blue);color:var(--white);font-size:19px;font-weight:500;text-align:center;line-height:37px}
.hero-bar{position:absolute;left:299px;top:444px;width:600px;height:36px;background:rgba(20,20,20,.7);color:var(--white)}
.hero-address{position:absolute;left:6px;top:9px;font-size:15px;font-weight:700}
.hero-details{position:absolute;left:365px;top:10px;font-size:13px}
.hero-price{position:absolute;left:443px;top:0;width:78px;height:36px;background:var(--blue);font-size:16px;font-weight:700;text-align:center;line-height:36px}
.hero-arrow{position:absolute;top:0;width:39px;height:36px;background:var(--orange);display:flex;align-items:center;justify-content:center}

/* recent */
.recent{top:605px;height:364px;background:radial-gradient(ellipse at 50% 40%,#e8f6f9 0%,#c6e6ee 60%,#b3dce6 100%)}
.section-title{position:absolute;left:0;width:1200px;text-align:center;font-weight:500}
.section-title.orange{color:var(--orange)}
.section-title.white{color:var(--white)}
.underline{position:absolute;height:2px;background:var(--blue)}
.carousel-arrow{position:absolute;width:26px;height:26px;border-radius:50%;background:rgba(255,255,255,.6);display:flex;align-items:center;justify-content:center}
.prop-card{position:absolute;top:61px;width:187px;height:287px;background:var(--orange-soft)}
.prop-head{height:30px;background:var(--orange);color:var(--white);font-size:11px;padding:9px 9px;display:flex;justify-content:space-between}
.prop-photo{height:113px}
.prop-band{height:61px;background:var(--blue);color:var(--white);position:relative;padding:18px 20px 0}
.prop-band .name{font-size:12px;font-weight:700}
.prop-band .price{font-size:12px;font-weight:700;margin-top:5px}
.prop-avatar{position:absolute;left:77px;top:-16px;width:32px;height:32px;border-radius:50%;border:3px solid var(--white);background:linear-gradient(#9bb3c6,#5b7894)}
.prop-stats{padding:12px 20px 0;color:var(--white);font-size:11px}
.prop-stats div{display:flex;justify-content:space-between;line-height:20px}

/* welcome */
.welcome{top:969px;height:342px;background:linear-gradient(180deg,#2b2724 0%,#3e3630 45%,#1f1c19 100%)}
.welcome-title{position:absolute;left:303px;top:24px;color:var(--white);font-size:25px;font-weight:500}
.welcome-sub{position:absolute;left:303px;top:52px;color:var(--white);font-size:18px;font-weight:500}
.step{position:absolute;top:96px;width:240px;text-align:center}
.step-icon{width:86px;height:86px;margin:0 auto;border:3px solid var(--white);border-radius:50%;background:rgba(0,0,0,.25);display:flex;align-items:center;justify-content:center}
.step-title{color:var(--blue-bright);font-size:20px;margin-top:28px}
.step-text{color:var(--white);font-size:9px;line-height:12px;margin:12px auto 0;width:130px}

/* easy */
.easy{top:1311px;height:301px;background:radial-gradient(circle at 15% 30%,rgba(255,255,255,.6) 0 60px,transparent 61px),radial-gradient(circle at 88% 20%,rgba(255,255,255,.5) 0 80px,transparent 81px),radial-gradient(circle at 95% 85%,rgba(3,146,205,.45) 0 70px,transparent 71px),linear-gradient(180deg,#dcebf2,#c3dde9)}
.feature{position:absolute;top:58px;width:200px;text-align:center}
.feature svg{display:block;margin:0 auto}
.feature-title{color:var(--orange);font-size:13px;font-weight:700;margin-top:12px}
.feature-text{color:#7a8a93;font-size:10px;line-height:13px;width:150px;margin:6px auto 0}

/* agents */
.agents{top:1612px;height:301px;background:linear-gradient(135deg,#2f9bf2 0%,#1a7fe6 50%,#0b66d4 100%)}
.agent{position:absolute;top:87px;width:139px;height:177px;background:var(--orange);border:2px solid #f5b58d}
.agent-photo{height:98px}
.agent-name{color:var(--white);font-size:9px;text-align:center;margin-top:5px}
.agent-loc{color:var(--white);font-size:8px;text-align:center;margin-top:3px}
.agent-btn{width:112px;height:19px;margin:8px auto 0;background:var(--blue);color:var(--white);font-size:9px;text-align:center;line-height:19px}

/* partners */
.partners{top:1913px;height:170px;background:var(--white)}
.partner{position:absolute;top:92px;height:46px}

/* testimonials */
.testimonials{top:2083px;height:270px;background:linear-gradient(135deg,#2f9bf2 0%,#1a7fe6 50%,#0b66d4 100%)}
.t-avatar{position:absolute;left:557px;top:70px;width:86px;height:86px;border-radius:50%;border:3px solid var(--white);background:linear-gradient(#f4f4f4,#cfd3d8)}
.t-name{position:absolute;left:0;width:1200px;top:161px;text-align:center;color:var(--white);font-size:16px}
.t-quote{position:absolute;left:0;width:1200px;top:202px;text-align:center;color:var(--white);font-size:16px;line-height:22px}
.t-arrow{position:absolute;top:123px;width:42px;height:42px;border:2px solid rgba(255,255,255,.8);border-radius:50%;display:flex;align-items:center;justify-content:center}

/* footer */
.footer{top:2353px;height:207px;background:var(--footer)}
.f-card{position:absolute;top:17px;width:188px;height:178px;background:var(--footer-card);border-top:3px solid var(--blue);color:#ddd}
.f-card h4{font-size:10px;font-weight:700;color:var(--white);padding:18px 16px 0}
.f-small{font-size:7px;line-height:9px;color:#c9c9c9}
.f-input{position:absolute;left:8px;top:10px;width:172px;height:18px;border:1px solid #777;font-size:8px;color:#bbb;padding:3px 6px}
.f-signup{position:absolute;right:0;top:0;width:48px;height:16px;background:var(--orange);color:var(--white);font-size:8px;text-align:center;line-height:16px}
.contact-row{position:absolute;left:16px;width:156px}
.contact-row .label{height:25px;background:var(--orange);color:var(--white);font-size:7px;padding:8px 8px;position:relative}
.contact-row .label::after{content:"";position:absolute;left:18px;bottom:-5px;border-left:5px solid transparent;border-right:5px solid transparent;border-top:5px solid var(--orange)}
.contact-row .value{height:23px;background:#555;color:#ddd;font-size:7px;padding:8px 8px}
.bottom-bar{top:2560px;height:49px;background:var(--brown)}
.copyright{position:absolute;left:333px;top:18px;color:#e6d5c9;font-size:8px}
.bottom-bar .social{left:756px;top:12px;gap:10px}
.bottom-bar .social span{width:24px;height:24px}
</style>
</head>
<body>

<header class="section topbar">
  <div class="social" role="img" aria-label="Social network links">
    <span></span><span></span><span></span><span></span>
  </div>
  <div class="top-links">
    <span><svg width="10" height="11" viewBox="0 0 10 11"><circle cx="5" cy="3" r="2.5" fill="#eee"/><path d="M0 11a5 5 0 0 1 10 0z" fill="#eee"/></svg>Login</span>
    <span><svg width="12" height="12" viewBox="0 0 12 12"><circle cx="6" cy="6" r="5.3" fill="none" stroke="#eee"/></svg>Language</span>
  </div>
</header>

<nav class="section navbar">
  <div class="brand">
    <span class="brand-mark"></span>
    <span class="brand-name">Thornbury Lettings Managment Ltd</span>
  </div>
  <div class="main-nav">
    <span class="active">HOME</span><span>LANDLORDS</span><span>AGENCIES</span><span>ABOUT US</span><span>CONTACT</span>
  </div>
</nav>

<section class="section hero">
  <div class="abs" style="inset:0" role="img" aria-label="Photograph of terraced houses stacked on a hillside"></div>
  <h1 class="hero-title">Find Your Home</h1>
  <form class="search-panel">
    <div class="field" style="left:16px;top:14px;width:180px"><label>Keyword</label><div class="select">Any</div></div>
    <div class="field" style="left:209px;top:14px;width:180px"><label>Location</label><div class="select">Any</div></div>
    <div class="field" style="left:402px;top:14px;width:180px"><label>Property Type</label><div class="select">Any</div></div>
    <div class="field" style="left:16px;top:58px;width:82px"><label>Min bedrooms</label><div class="select">Any</div></div>
    <div class="field" style="left:112px;top:58px;width:82px"><label>Min Bathrooms</label><div class="select">Any</div></div>
    <div class="field" style="left:209px;top:58px;width:82px"><label>Min Area (Sq ft)</label><div class="select">Any</div></div>
    <div class="field" style="left:305px;top:58px;width:82px"><label>Max Area (Sq ft)</label><div class="select">Any</div></div>
    <div class="field" style="left:402px;top:58px;width:82px"><label>Min Price</label><div class="select">Any</div></div>
    <div class="field" style="left:499px;top:58px;width:82px"><label>Max Price</label><div class="select">Any</div></div>
    <span class="corner left"></span><span class="corner right"></span>
    <div class="search-btn">Search</div>
  </form>
  <div class="hero-bar">
    <span class="hero-address">7 Harbour Lane, Bristol, BS1 4QA</span>
    <span class="hero-details"><svg width="10" height="11" viewBox="0 0 10 11" style="vertical-align:-1px;margin-right:4px"><rect x=".5" y=".5" width="9" height="10" fill="none" stroke="#ddd"/><path d="M2 4h6M2 6h6M2 8h4" stroke="#ddd"/></svg>details</span>
    <span class="hero-price">$420.000</span>
    <span class="hero-arrow" style="left:521px"><svg width="7" height="10"><path d="M6 0L0 5l6 5z" fill="#fff"/></svg></span>
    <span class="hero-arrow" style="left:561px;border-left:1px solid #e07a3b"><svg width="7" height="10"><path d="M1 0l6 5-6 5z" fill="#fff"/></svg></span>
  </div>
</section>

<section class="section recent">
  <h2 class="section-title orange" style="top:16px;font-size:25px">Recent Properties</h2>
  <span class="underline" style="left:500px;top:50px;width:76px"></span>
  <span class="carousel-arrow" style="left:268px;top:148px"><svg width="7" height="10"><path d="M6 0L0 5l6 5z" fill="#fff"/></svg></span>
  <span class="carousel-arrow" style="left:906px;top:148px"><svg width="7" height="10"><path d="M1 0l6 5-6 5z" fill="#fff"/></svg></span>

  <article class="prop-card" style="left:299px">
    <div class="prop-head"><span>Actions</span><span>&#9825;</span></div>
    <div class="prop-photo" role="img" aria-label="Photograph of an apartment block" style="background:linear-gradient(#9fa8b0,#6f7377)"></div>
    <div class="prop-band"><span class="prop-avatar" role="img" aria-label="Agent portrait"></span><div class="name">Lamb Dale</div><div class="price">$220,000</div></div>
    <div class="prop-stats"><div><span>Baths</span><span>1</span></div><div><span>Beds</span><span>2</span></div><div><span>Area</span><span>100 sqft</span></div></div>
  </article>
  <article class="prop-card" style="left:506px">
    <div class="prop-head"><span>Actions</span><span>&#9825;</span></div>
    <div class="prop-photo" role="img" aria-label="Photograph of a white period building" style="background:linear-gradient(#c9d7e4,#b7b1a6)"></div>
    <div class="prop-band"><span class="prop-avatar" role="img" aria-label="Agent portrait"></span><div class="name">Cotton Ridge</div><div class="price">$340,000</div></div>
    <div class="prop-stats"><div><span>Baths</span><span>3</span></div><div><span>Beds</span><span>3</span></div><div><span>Area</span><span>300 sqft</span></div></div>
  </article>
  <article class="prop-card" style="left:713px">
    <div class="prop-head"><span>Actions</span><span>&#9825;</span></div>
    <div class="prop-photo" role="img" aria-label="Aerial photograph of a housing estate" style="background:linear-gradient(#8d8a78,#5f5a4c)"></div>
    <div class="prop-band"><span class="prop-avatar" role="img" aria-label="Agent portrait"></span><div class="name">Apricot Alcove</div><div class="price">$220,000</div></div>
    <div class="prop-stats"><div><span>Baths</span><span>3</span></div><div><span>Beds</span><span>4</span></div><div><span>Area</span><span>175 sqft</span></div></div>
  </article>
</section>

<section class="section welcome">
  <div class="abs" style="inset:0" role="img" aria-label="Darkened photograph of a suburban street"></div>
  <h2 class="welcome-title">Welcome</h2>
  <p class="welcome-sub">The standard chunk of Lorem Ipsum used since</p>

  <div class="step" style="left:254px">
    <div class="step-icon"><svg width="44" height="44" viewBox="0 0 44 44"><circle cx="22" cy="13" r="9" fill="#fff"/><path d="M4 42c0-12 8-18 18-18s18 6 18 18z" fill="#fff"/><path d="M22 25l-3 4 3 11 3-11z" fill="#333"/></svg></div>
    <div class="step-title">Register</div>
    <p class="step-text">"Neque porro quisquam est qui dolorem ipsum quia dolor sit amet, consectetur, velit..." "There is no one who loves pain itself, who seeks after it and wants to have it, simply because it is pain..."</p>
  </div>
  <div class="step" style="left:483px">
    <div class="step-icon"><svg width="44" height="44" viewBox="0 0 44 44"><path d="M8 4h20l6 6v28H8z" fill="none" stroke="#fff" stroke-width="3"/><path d="M13 14h14M13 20h10" stroke="#fff" stroke-width="3"/><circle cx="27" cy="28" r="6" fill="none" stroke="#fff" stroke-width="3"/><path d="M31 32l6 6" stroke="#fff" stroke-width="4"/></svg></div>
    <div class="step-title">Fill Up Property Details</div>
    <p class="step-text">"Neque porro quisquam est qui dolorem ipsum quia dolor sit amet, consectetur, velit..." "There is no one who loves pain itself, who seeks after it and wants to have it, simply because it is pain..."</p>
  </div>
  <div class="step" style="left:703px">
    <div class="step-icon"><svg width="44" height="44" viewBox="0 0 44 44"><path d="M6 24l11 11L39 9" fill="none" stroke="#fff" stroke-width="7"/></svg></div>
    <div class="step-title">You are Done!</div>
    <p class="step-text">Lorem ipsum dolor sit amet, consectetur adipiscing elit, sed do eiusmod tempor incididunt ut labore et dolore magna aliqua. Ut enim ad minim veniam</p>
  </div>
</section>

<section class="section easy">
  <h2 class="section-title orange" style="top:18px;font-size:23px">We make your life easy. Heres how.</h2>

  <div class="feature" style="left:282px">
    <svg width="84" height="90" viewBox="0 0 90 96"><path d="M45 93l-8-10a42 42 0 1 1 16 0z" fill="none" stroke="var(--blue)" stroke-width="1.5"/><path d="M33 22h18l8 8v32H33z" fill="var(--blue)"/><path d="M38 36h16M38 42h16M38 48h12" stroke="#fff" stroke-width="2"/></svg>
    <div class="feature-title">HOTTEST LISTINGS</div>
    <p class="feature-text">Lorem ipsum dolor sit amet, consectetur adipiscing. In metus diam, fermentum in orci sit amet, lobortis congue diam. Interdum et malesuada fames ac ante ipsum primis in faucibus.</p>
  </div>
  <div class="feature" style="left:500px">
    <svg width="84" height="90" viewBox="0 0 90 96"><path d="M45 93l-8-10a42 42 0 1 1 16 0z" fill="none" stroke="var(--blue)" stroke-width="1.5"/><circle cx="45" cy="42" r="17" fill="none" stroke="var(--blue)" stroke-width="4"/><path d="M53 34l-5 12-11 4 5-12z" fill="var(--blue)"/></svg>
    <div class="feature-title">KNOWLEDGABLE AGENTS</div>
    <p class="feature-text">Lorem ipsum dolor sit amet, consectetur adipiscing. In metus diam, fermentum in orci sit amet, lobortis congue diam. Interdum et malesuada fames ac ante ipsum primis in faucibus.</p>
  </div>
  <div class="feature" style="left:718px">
    <svg width="84" height="90" viewBox="0 0 90 96"><path d="M45 93l-8-10a42 42 0 1 1 16 0z" fill="none" stroke="var(--blue)" stroke-width="1.5"/><circle cx="45" cy="34" r="9" fill="var(--blue)"/><path d="M30 58c0-10 6-14 15-14s15 4 15 14z" fill="var(--blue)"/></svg>
    <div class="feature-title">EXPERT GUIDANCE</div>
    <p class="feature-text">Lorem ipsum dolor sit amet, consectetur adipiscing. In metus diam, fermentum in orci sit amet, lobortis congue diam. Interdum et malesuada fames ac ante ipsum primis in faucibus.</p>
  </div>
</section>

<section class="section agents">
  <h2 class="section-title white" style="top:23px;font-size:28px">OUR AGENTS</h2>
  <span class="underline" style="left:536px;top:62px;width:44px;background:var(--white);opacity:.6"></span>
  <article class="agent" style="left:299px">
    <div class="agent-photo" role="img" aria-label="Portrait photograph of agent" style="background:linear-gradient(#e9d9c7,#b9946f)"></div>
    <div class="agent-name">Marta Kowal</div><div class="agent-loc">Manchester UK</div><div class="agent-btn">View Profile</div>
  </article>
  <article class="agent" style="left:454px">
    <div class="agent-photo" role="img" aria-label="Portrait photograph of agent" style="background:linear-gradient(#f4f4f4,#c8c2bb)"></div>
    <div class="agent-name">Daniel Pryce</div><div class="agent-loc">Durham UK</div><div class="agent-btn">View Profile</div>
  </article>
  <article class="agent" style="left:607px">
    <div class="agent-photo" role="img" aria-label="Portrait photograph of agent" style="background:linear-gradient(#f2efec,#a8826a)"></div>
    <div class="agent-name">Sofia Lind</div><div class="agent-loc">Manchester UK</div><div class="agent-btn">View Profile</div>
  </article>
  <article class="agent" style="left:760px">
    <div class="agent-photo" role="img" aria-label="Portrait photograph of agent" style="background:linear-gradient(#fafafa,#c6c9ce)"></div>
    <div class="agent-name">Owen Hale</div><div class="agent-loc">Durham UK</div><div class="agent-btn">View Profile</div>
  </article>
</section>

<section class="section partners">
  <h2 class="section-title orange" style="top:25px;font-size:28px">OUR PARTNERS</h2>
  <span class="underline" style="left:500px;top:66px;width:58px"></span>
  <span class="partner" role="img" aria-label="DWF membership badge" style="left:299px;width:78px;background:#8d1c2b"></span>
  <span class="partner" role="img" aria-label="KTB membership badge" style="left:410px;width:38px;background:#2b8a72;border-radius:4px"></span>
  <span class="partner" role="img" aria-label="GMV membership badge" style="left:466px;width:178px;background:#7a4f9c"></span>
  <span class="partner" role="img" aria-label="safehold-example.co.uk membership badge" style="left:660px;width:242px;background:#1aa7b8"></span>
</section>

<section class="section testimonials">
  <h2 class="section-title white" style="top:21px;font-size:28px">TESTIMONIALS</h2>
  <span class="t-arrow" style="left:257px"><svg width="10" height="14"><path d="M8 1L2 7l6 6" fill="none" stroke="#fff" stroke-width="1.5"/></svg></span>
  <span class="t-arrow" style="left:901px"><svg width="10" height="14"><path d="M2 1l6 6-6 6" fill="none" stroke="#fff" stroke-width="1.5"/></svg></span>
  <span class="t-avatar" role="img" aria-label="Portrait photograph of client"></span>
  <p class="t-name">Tom Ashcroft</p>
  <p class="t-quote">Thank you very much. I'm impressed with your service. I've already told<br>my friends about your site and your quick response, thanks again!</p>
</section>

<footer class="section footer">
  <div class="f-card" style="left:299px">
    <h4>Recent Posts</h4>
    <p class="f-small" style="padding:14px 16px 0">New</p>
    <p style="font-size:9px;color:#eee;padding:14px 16px 0">12 Harbour Row, Clifton</p>
    <p class="f-small" style="padding:14px 16px 0">Sed auctor aliquet. Aenean sollicitudin, lorem quis bibendum auctor, nisi elit consequat ipsum, nec sagittis sem nibh id elit. Duis sed odio sit amet nibh vulputate cursus a sit amet mauris. Morbi accumsan ipsum velit.</p>
  </div>
  <div class="f-card" style="left:506px">
    <div class="f-input">&#9993; Email Address<span class="f-signup">Sign Up</span></div>
    <span class="abs" role="img" aria-label="Company emblem" style="left:68px;top:46px;width:52px;height:20px;background:#c8242b"></span>
    <p class="f-small abs" style="left:16px;top:84px;width:156px;text-align:center">This is Layoutpad's version of Lorem Ipsum. Proin gravida nibh vel velit auctor aliquet. Aenean sollicitudin, lorem quis bibendum auctor, nisi elit consequat ipsum, nec sagittis sem nibh id elit.</p>
  </div>
  <div class="f-card" style="left:713px">
    <h4>Contact Us</h4>
    <div class="contact-row" style="top:46px"><div class="label">Make a Call</div><div class="value">0117 496 0321</div></div>
    <div class="contact-row" style="top:104px"><div class="label">Send us an Email</div><div class="value">hello@thornbury.example</div></div>
  </div>
</footer>

<div class="section bottom-bar">
  <p class="copyright">&copy; 2016 All Rights Reserved Terms of Use and Privacy Policy</p>
  <svg class="abs" style="left:581px;top:8px" width="34" height="34" viewBox="0 0 34 34"><circle cx="17" cy="17" r="15" fill="none" stroke="#eee" stroke-width="2"/><path d="M10 22l7-10 7 10" fill="none" stroke="#eee" stroke-width="2.5"/></svg>
  <div class="social" role="img" aria-label="Social network links">
    <span></span><span></span><span></span><span></span>
  </div>
</div>

</body>
</html>
```